Technical audit needs a report template

As our company runs various technical audits, we also provide findings on paper, online or in Powerpoint. For this reason we need an identity pack, which includes business cards, complimentary cards, letterhead and the likes.

Who would be up to create this stationery pack for us? We hope to receive a style for these documents, that look professional and can be easily extended.
Updates

Project Deadline Extended Reason: I would like to provide the opportunity to friended designers to submit their designs too! Added Sunday, October 9, 2016

Target Market(s)

Start-ups, scale-ups and investors

Industry/Entity Type

Investment

Contact Information for Business Card

Street: Lindenhoutkade 42
Postcode: 3617KW
City: Utrecht
Country: The Netherlands
Phone: +31 302849516
Cell Phone: +31 6 58193074
email: jeroen@vexomari.example
website: https://vexomari.example

Requirements
Must have
• I don't have inspiration, should just be a slick design based on the logo provided.
Nice to have
• Logo could be on the back of the card?
Should not have
• Should not use different colours then the logo, or at least fit the colour scheme.

```html
<!DOCTYPE html>
<html lang="en">
<head>
<meta charset="utf-8">
<title>Vexomari – Business Card</title>
<link href="https://fonts.googleapis.com/css2?family=Lato:wght@400;700;900&display=swap" rel="stylesheet">
<style>
  :root {
    --brand-blue: #1ea4cb;
    --brand-blue-dark: #1488ab;
    --card-dark: #474748;
    --card-white: #ffffff;
    --text-light: #f2f2f2;
    --text-dark: #2e2e30;
    --backdrop: #e9e7e3;
  }
  * { box-sizing: border-box; margin: 0; padding: 0; }
  html, body {
    width: 1200px; height: 950px; overflow: hidden;
    background: var(--backdrop);
    font-family: "Lato", sans-serif;
  }
  .card-set {
    position: absolute; inset: 0;
    display: flex; align-items: center; justify-content: center; gap: 90px;
  }
  .card {
    width: 380px; height: 664px;
    border: 12px solid var(--brand-blue);
    box-shadow: 0 6px 18px rgba(0,0,0,.18);
    position: relative;
  }
  .card--front { background: var(--card-dark); color: var(--text-light); }
  .card--back  { background: var(--card-white); }

  .holder {
    position: absolute; top: 62px; left: 42px;
    display: flex; align-items: flex-start; gap: 12px;
  }
  .holder__mark {
    width: 36px; height: 36px; border: 4px solid var(--brand-blue); flex: none;
  }
  .holder__name {
    color: var(--brand-blue); font-weight: 900; font-size: 21px;
    letter-spacing: 1px; line-height: 1.05;
  }
  .holder__role { font-size: 17px; margin-top: 3px; }

  .contact {
    position: absolute; top: 200px; left: 0; right: 0;
    list-style: none; text-align: center; font-size: 17px; line-height: 1.3;
  }
  .contact__item { margin-bottom: 10px; }
  .contact__icon { display: block; margin: 0 auto 6px; width: 16px; height: 16px; }

  .brand {
    position: absolute; inset: 0;
    display: flex; flex-direction: column; align-items: center; justify-content: center; gap: 28px;
  }
  .brand__square { width: 120px; height: 120px; background: var(--brand-blue); }
  .brand__name {
    color: var(--text-dark); font-weight: 900; font-size: 46px; letter-spacing: 3px;
  }
</style>
</head>
<body>
<main class="card-set">
  <section class="card card--front" aria-label="Business card front">
    <div class="holder">
      <span class="holder__mark"></span>
      <div>
        <p class="holder__name">JEROEN VERMAAT</p>
        <p class="holder__role">CEO/Founder</p>
      </div>
    </div>

    <ul class="contact">
      <li class="contact__item">
        <svg class="contact__icon" viewBox="0 0 16 16" aria-hidden="true"><path d="M8 1a5 5 0 0 0-5 5c0 4 5 9 5 9s5-5 5-9a5 5 0 0 0-5-5zm0 7a2 2 0 1 1 0-4 2 2 0 0 1 0 4z" fill="var(--brand-blue)"/></svg>
        Lindenhoutkade 42<br>Utrecht, The Netherlands 3617KW
      </li>
      <li class="contact__item">
        <svg class="contact__icon" viewBox="0 0 16 16" aria-hidden="true"><path d="M3 1h3l1.5 4-2 1.3a9 9 0 0 0 4.2 4.2L11 8.5l4 1.5v3a2 2 0 0 1-2 2C7 15 1 9 1 3a2 2 0 0 1 2-2z" fill="var(--brand-blue)"/></svg>
        +31 302849516
      </li>
      <li class="contact__item">
        <svg class="contact__icon" viewBox="0 0 16 16" aria-hidden="true"><rect x="4" y="1" width="8" height="14" rx="1.5" fill="none" stroke="var(--brand-blue)" stroke-width="1.8"/><circle cx="8" cy="12.5" r="0.9" fill="var(--brand-blue)"/></svg>
        +31 6 58193074
      </li>
      <li class="contact__item">
        <svg class="contact__icon" viewBox="0 0 16 16" aria-hidden="true"><rect x="1" y="3" width="14" height="10" rx="1" fill="var(--brand-blue)"/><path d="M1.5 4l6.5 5 6.5-5" fill="none" stroke="var(--card-dark)" stroke-width="1.2"/></svg>
        jeroen@vexomari.example
      </li>
      <li class="contact__item">
        <svg class="contact__icon" viewBox="0 0 16 16" aria-hidden="true"><circle cx="8" cy="8" r="7" fill="var(--brand-blue)"/><path d="M1 8h14M8 1c-3 3.5-3 10.5 0 14M8 1c3 3.5 3 10.5 0 14" fill="none" stroke="var(--card-dark)" stroke-width="1"/></svg>
        vexomari.example
      </li>
    </ul>
  </section>

  <section class="card card--back" aria-label="Business card back">
    <div class="brand">
      <span class="brand__square"></span>
      <p class="brand__name">VEXOMARI</p>
    </div>
  </section>
</main>
</body>
</html>
```